Business Card for Freelance Copywriting & Web Design Business

Hi! I have a logo but want a new business card. Here's a better idea of what I'm thinking:
-Brand new double-sided business card, rounded cards, embossed logo, nice quality paper
-Include phone (604-382-5194), email (hello@lauraberndt.org), and website (www.lauraberndt.org). No address, please, since I service clients worldwide.
-I'd like the fonts to match those on my website (www.lauraberndt.org). I had to purchase the one font (Born Ready), attached. I'm not sure which version was used on my site so I included all that I purchased. The secondary font is Helvetica
-I'd also like the tagline "Powerful Words. Impressive Results." included.
-My primary brand colour is the teal, colour #19ADC3
Laura Berndt | Laura Berndt Copywriting & Web Design <hello@lauraberndt.org>
-I'd also like the following services listed on the new cards:
SEO Website Content
SEO Blog Content
SEO Website Design
Contact Information for Business Card
as stated in brief
Font styles to use
Other font styles liked:
- See brief
Look and feel
Each slider illustrates characteristics of the customer's brand and the style your logo design should communicate.

```html
<!DOCTYPE html>
<html lang="en">
<head>
<meta charset="UTF-8">
<title>Laura Berndt Copywriting &amp; Web Design – Business Card</title>
<link href="https://fonts.googleapis.com/css2?family=Montserrat:wght@400;500;700;800&display=swap" rel="stylesheet">
<style>
  :root {
    --teal: #19adc3;
    --feather-light: #b9dfe6;
    --feather-mid: #86c4cf;
    --ink: #1c1c1c;
    --card-white: #ffffff;
    --card-black: #161616;
    --emboss: #4a4a4a;
    --emboss-light: #8a8a8a;
    --backdrop-top: #cfcfcf;
    --backdrop-bottom: #a9a9a9;
    --text-light: #ffffff;
  }
  * { margin: 0; padding: 0; box-sizing: border-box; }
  html, body { width: 1200px; height: 815px; overflow: hidden; }
  body {
    background: linear-gradient(180deg, var(--backdrop-top), var(--backdrop-bottom));
    font-family: "Montserrat", Helvetica, Arial, sans-serif;
    position: relative;
  }
  .card {
    position: absolute;
    top: 253px;
    width: 540px;
    height: 309px;
    border-radius: 26px;
    overflow: hidden;
    box-shadow: 0 5px 0 var(--teal), 0 18px 30px rgba(0,0,0,0.28);
  }
  .card--front { left: 40px; background: var(--card-white); }
  .card--back { left: 620px; background: var(--card-black); }

  /* front */
  .feather-art {
    position: absolute;
    right: 22px;
    top: 26px;
    width: 168px;
    height: 200px;
    border-radius: 60% 40% 55% 45%;
    background: radial-gradient(ellipse at 40% 35%, var(--feather-light), var(--feather-mid) 70%, rgba(134,196,207,0) 72%);
  }
  .front-identity { position: absolute; left: 38px; top: 66px; }
  .brand-name {
    font-weight: 500;
    font-size: 36px;
    color: var(--teal);
    line-height: 1;
    letter-spacing: 0.5px;
  }
  .brand-tagline {
    margin-top: 10px;
    font-weight: 800;
    font-size: 11.5px;
    letter-spacing: 2.4px;
    color: var(--ink);
  }
  .slogan {
    margin-top: 22px;
    font-size: 13px;
    line-height: 1.35;
    color: var(--ink);
  }
  .slogan strong { font-weight: 700; color: var(--teal); }
  .contact-list { list-style: none; margin-top: 18px; }
  .contact-list li {
    display: flex;
    align-items: center;
    gap: 9px;
    font-size: 13.5px;
    line-height: 1.55;
    color: var(--ink);
  }
  .contact-icon { width: 12px; height: 12px; flex: none; }

  /* back */
  .feather-art--faint {
    position: absolute;
    left: 210px;
    right: auto;
    top: 20px;
    width: 220px;
    height: 200px;
    border-radius: 55% 45% 50% 50%;
    background: radial-gradient(ellipse at 50% 40%, #2e3133, rgba(30,30,30,0) 70%);
  }
  .back-identity { position: absolute; left: 0; right: 0; top: 88px; text-align: center; }
  .back-identity .brand-name { color: var(--emboss-light); font-size: 46px; }
  .back-identity .brand-tagline {
    color: var(--emboss);
    font-weight: 700;
    font-size: 15px;
    letter-spacing: 4.5px;
    margin-top: 14px;
  }
  .service-list {
    position: absolute;
    left: 0; right: 0;
    bottom: 34px;
    display: flex;
    justify-content: center;
    align-items: center;
    gap: 9px;
    list-style: none;
    color: var(--text-light);
    font-size: 13.5px;
    letter-spacing: 0.4px;
  }
  .service-dot { width: 5px; height: 5px; border-radius: 50%; background: var(--teal); }
</style>
</head>
<body>
  <section class="card card--front" aria-label="Business card front">
    <div class="feather-art" role="img" aria-label="Soft teal feather illustration"></div>
    <div class="front-identity">
      <div class="brand-name">Laura Berndt</div>
      <div class="brand-tagline">COPYWRITING &amp; WEB DESIGN</div>
      <p class="slogan"><strong>Powerful Words. Impressive Results.</strong><br>(Supporting Clients Worldwide)</p>
      <ul class="contact-list">
        <li>
          <svg class="contact-icon" viewBox="0 0 12 12" aria-hidden="true"><path d="M2.5 1 L4.3 1 L5 3.6 L3.9 4.4 Q4.8 6.6 7.3 8 L8.2 7 L11 7.6 L11 9.5 Q10.8 11 9.3 11 Q2 10 1 2.8 Q1 1 2.5 1Z" fill="var(--teal)"/></svg>
          604-382-5194
        </li>
        <li>
          <svg class="contact-icon" viewBox="0 0 12 12" aria-hidden="true"><rect x="0.5" y="2.5" width="11" height="7.5" rx="1" fill="var(--teal)"/><path d="M0.8 3 L6 7 L11.2 3" stroke="#fff" stroke-width="1" fill="none"/></svg>
          hello@lauraberndt.org
        </li>
        <li>
          <svg class="contact-icon" viewBox="0 0 12 12" aria-hidden="true"><circle cx="6" cy="6" r="5.5" fill="var(--teal)"/><path d="M0.5 6 H11.5 M6 0.5 V11.5 M2 3 Q6 4.5 10 3 M2 9 Q6 7.5 10 9" stroke="#fff" stroke-width="0.7" fill="none"/></svg>
          www.lauraberndt.org
        </li>
      </ul>
    </div>
  </section>

  <section class="card card--back" aria-label="Business card back">
    <div class="feather-art feather-art--faint" role="img" aria-label="Faint embossed feather illustration"></div>
    <div class="back-identity">
      <div class="brand-name">Laura Berndt</div>
      <div class="brand-tagline">COPYWRITING &amp; WEB DESIGN</div>
    </div>
    <ul class="service-list">
      <li>SEO Website Content</li>
      <li class="service-dot" aria-hidden="true"></li>
      <li>SEO Blog Content</li>
      <li class="service-dot" aria-hidden="true"></li>
      <li>SEO Website Design</li>
    </ul>
  </section>
</body>
</html>
```